Brindle Works Ltd

I'd like to create a company letterhead for the attached logo in word format.

I'd like to emphasis the icon in large translucent state from the left corner and ensure that the letterhead colouring matches the colour palette of the current logo with a contrast so it's clear to see. I've attached a copy of our sister company page on the app for reference.

```html
<!DOCTYPE html>
<html lang="en">
<head>
<meta charset="utf-8">
<title>Brindle Works Ltd – Letterhead</title>
<link rel="stylesheet" href="https://fonts.googleapis.com/css2?family=Roboto:wght@400;500;700&family=Montserrat:wght@500&display=swap">
<style>
  :root {
    --teal: #00b8a2;
    --teal-1: #1fc4b0;
    --teal-2: #45cfbe;
    --teal-3: #6cdacd;
    --teal-4: #90e3d9;
    --teal-5: #b2ece5;
    --teal-6: #d5f5f0;
    --wash: #e4f6f3;
    --ink: #4a4a4a;
    --ink-dark: #555;
    --paper: #ffffff;
    --footer-bg: #f2f2f2;
    --stage: #eeeeee;
  }
  * { box-sizing: border-box; margin: 0; padding: 0; }
  html, body { width: 1200px; height: 1200px; overflow: hidden; }
  body {
    background: var(--stage);
    font-family: "Roboto", Arial, sans-serif;
    position: relative;
  }
  .letterhead {
    position: absolute;
    left: 197px;
    top: 30px;
    width: 806px;
    height: 1140px;
    background: var(--paper);
    overflow: hidden;
    box-shadow: 0 10px 30px rgba(0,0,0,0.12);
  }
  .backdrop-mark {
    position: absolute;
    left: -330px;
    top: 320px;
    width: 760px;
    height: 760px;
    border-radius: 50%;
    background: var(--wash);
    opacity: 0.8;
  }
  .brand {
    position: relative;
    display: flex;
    align-items: center;
    justify-content: center;
    gap: 12px;
    padding-top: 20px;
    height: 88px;
  }
  .brand-dot {
    width: 44px;
    height: 44px;
    border-radius: 50%;
    background: var(--teal);
  }
  .brand-name {
    font-family: "Montserrat", Arial, sans-serif;
    font-weight: 500;
    font-size: 30px;
    color: var(--teal);
    letter-spacing: 0.5px;
  }
  .letter-body {
    position: relative;
    margin: 30px 95px 0;
    color: var(--ink);
    font-size: 15.3px;
    line-height: 26.4px;
    text-align: justify;
  }
  .letter-body p + p { margin-top: 26px; }
  .sign-off {
    position: absolute;
    right: 95px;
    top: 873px;
    width: 296px;
    text-align: right;
  }
  .sign-line { border-top: 1.5px solid #a8a8a8; }
  .sign-name {
    margin-top: 14px;
    font-weight: 700;
    font-size: 17px;
    color: var(--ink-dark);
    line-height: 1;
  }
  .sign-role {
    font-size: 11.5px;
    color: var(--ink-dark);
    line-height: 1.3;
  }
  .contact-bar {
    position: absolute;
    left: 0;
    right: 0;
    top: 1063px;
    height: 54px;
    background: var(--footer-bg);
    display: flex;
    align-items: center;
    padding-left: 136px;
  }
  .contact-item {
    display: flex;
    align-items: center;
    gap: 10px;
    font-size: 13.4px;
    line-height: 16px;
    color: var(--ink-dark);
  }
  .contact-item.address { width: 210px; }
  .contact-item.phone { width: 196px; }
  .contact-icon {
    width: 25px;
    height: 25px;
    border-radius: 5px;
    background: var(--teal);
    display: flex;
    align-items: center;
    justify-content: center;
    flex-shrink: 0;
  }
  .tone-strip {
    position: absolute;
    left: 0;
    right: 0;
    bottom: 0;
    height: 23px;
    display: flex;
  }
  .tone-strip span { flex: 1; }
</style>
</head>
<body>
  <main class="letterhead">
    <div class="backdrop-mark" aria-hidden="true"></div>

    <header class="brand">
      <div class="brand-dot" aria-hidden="true"></div>
      <div class="brand-name">Brindle Works Ltd</div>
    </header>

    <section class="letter-body">
      <p>Lorem ipsum dolor sit amet, consectetur adipiscing elit. Vivamus sed mi mi. Mauris sollicitudin ipsum eu nulla tempus dapibus. Aenean cursus erat in tempor consequat. In hac habitasse platea dictumst. Vivamus sollicitudin dapibus lorem, ut aliquam lorem lacinia sed. Praesent accumsan odio sit amet elit tempus, ut molestie diam laoreet. Fusce nec scelerisque mi. Suspendisse in mauris eget purus gravida porttitor a vitae nibh.</p>
      <p>Phasellus nec dolor convallis, semper lectus sit amet, congue elit. Mauris eget dolor nunc. Phasellus vitae ante nec ligula feugiat scelerisque. Proin eu condimentum nisl. Ut magna leo, tincidunt a magna feugiat, pellentesque porttitor lacus. Mauris id urna posuere, dignissim enim eget, egestas augue. Aliquam eleifend vehicula eleifend. Mauris lacus nibh, ullamcorper at ipsum et, sodales feugiat diam. Vestibulum ultricies quis elit vel aliquam. Aliquam sagittis lorem quam. Interdum et malesuada fames ac ante ipsum primis in faucibus. Vivamus hendrerit ante eget congue feugiat.</p>
      <p>Mauris varius pretium porttitor. Morbi ultrices, metus ac fringilla placerat, dui orci ornare tellus, non vulputate velit turpis ac ipsum. Morbi interdum augue sed magna luctus, quis mollis nunc commodo. Quisque vehicula iaculis neque ut mollis. Cras consequat, nisi sit amet interdum pharetra, leo felis cursus ante, eu pharetra mi turpis a eros. Fusce non enim ut mi ultricies pellentesque vel et nisl. Nullam venenatis suscipit risus, sit amet mattis lorem pharetra vitae. In commodo quam non dolor volutpat, vel posuere dui tincidunt. Duis ullamcorper neque sit amet elit iaculis, in tincidunt orci cursus. Nunc sit amet mauris tortor. Mauris convallis id ligula sed viverra. Sed aliquam, ante sed aliquam convallis, nulla leo feugiat neque, a fermentum massa est nec mi. Duis ligula est scelerisque eu volutpat vel, interdum id ligula. Nullam ac vestibulum tellus. Donec venenatis porttitor lacus, at malesuada ex pretium vel.</p>
    </section>

    <div class="sign-off">
      <div class="sign-line"></div>
      <div class="sign-name">Mara Ellison</div>
      <div class="sign-role">Director</div>
    </div>

    <footer class="contact-bar">
      <div class="contact-item address">
        <div class="contact-icon">
          <svg width="13" height="16" viewBox="0 0 13 16" aria-hidden="true"><path d="M6.5 0.5C3.2 0.5 0.8 3 0.8 6.1c0 4 5.7 9.4 5.7 9.4s5.7-5.4 5.7-9.4C12.2 3 9.8 0.5 6.5 0.5z" fill="#fff"/><circle cx="6.5" cy="6" r="2.2" fill="#00b8a2"/></svg>
        </div>
        <div>Suite 4, Harbour Lane<br>Dock Quarter, 60718</div>
      </div>
      <div class="contact-item phone">
        <div class="contact-icon">
          <svg width="15" height="15" viewBox="0 0 24 24" aria-hidden="true"><path d="M6.6 10.8c1.4 2.8 3.8 5.1 6.6 6.6l2.2-2.2c.3-.3.7-.4 1-.2 1.1.4 2.3.6 3.6.6.6 0 1 .4 1 1V20c0 .6-.4 1-1 1C10.6 21 3 13.4 3 4c0-.6.4-1 1-1h3.5c.6 0 1 .4 1 1 0 1.3.2 2.5.6 3.6.1.3 0 .7-.2 1l-2.3 2.2z" fill="#fff"/></svg>
        </div>
        <div>+ 555 0140 0192<br>(01) 632 0187 0144</div>
      </div>
      <div class="contact-item web">
        <div class="contact-icon">
          <svg width="15" height="15" viewBox="0 0 16 16" aria-hidden="true"><circle cx="6.5" cy="6.5" r="4.3" fill="none" stroke="#fff" stroke-width="2"/><path d="M9.6 9.6l4.6 4.6" stroke="#fff" stroke-width="2.4" stroke-linecap="round"/></svg>
        </div>
        <div>hello@brindleworks.com<br>www.brindleworks.com</div>
      </div>
    </footer>

    <div class="tone-strip" aria-hidden="true">
      <span style="background: var(--teal)"></span>
      <span style="background: var(--teal-1)"></span>
      <span style="background: var(--teal-2)"></span>
      <span style="background: var(--teal-3)"></span>
      <span style="background: var(--teal-4)"></span>
      <span style="background: var(--teal-5)"></span>
      <span style="background: var(--teal-6)"></span>
    </div>
  </main>
</body>
</html>
```